Pimbrook

Squarespace website for specialty health based ingredients, like organic Galactose, CBD Oil, Hyaluronic Acid. Already have a logo that I want to use.

Reason: Too few designs submitted. I would like to see what other designers can do.

I am not sure that I am getting what I need. I was hoping for a fully working Squarespace Website and listed that as uncoded. But, I think that it has to be fully coded and then I import it to my SquareSpace to get the functional website and request that Velmora hosts the site. I mentioned that I want my office to be able to make revisions, etc but they will not know HTML nor be able convert it themselves. May I get an explanation? I do see several designs that I really like. But, am unclear exactly what I am purchasing and will eventually own.

Target Market(s)

Buyers of bulk chemicals used in the manufacture of pharmaceuticals, supplements, specialty foods and beverages.

Industry/Entity Type

Health And Wellness

Number of Pages Required

5+ page

Font styles to use
Sans Serif

Colors
33b8a4
add136
34a7d8

Requirements
Must have
• Please see Fernhollow Tonics, Inc website for the pages that I need. I want a similar set up for products, only for specialty usually plant-based chemicals. Mapping should be the same.
Nice to have
• Brief content on a sample product such as pure CBD Oil or Galactose (D+) as examples. I would like a SquareSpace design if possible so that my staff can make changes readily. Would like to have Velmora host the site once completed. Not sure what is Uncoded web design vs.Coded. Please help me know how to answer that question.
Should not have
• Please no association with Marijuana. This CBD Hemp Oil is 99.9% free of THC and imported into the United States legally. No people, needles, social networking, or newsletter necessary. Most of the designs are very tiny logos, could be bigger.

```html
<!DOCTYPE html>
<html lang="en">
<head>
<meta charset="utf-8">
<title>Pimbrook Inc. — Specialty Ingredients</title>
<link rel="stylesheet" href="https://fonts.googleapis.com/css2?family=Lato:wght@400;700&family=Jost:wght@400;500&display=swap">
<style>
:root{
  --green:#8dbf3e;
  --green-dark:#6f9e2c;
  --blue:#34a7d8;
  --navy:#1d5a99;
  --ink:#222;
  --text:#4a4a4a;
  --gray-bg:#ececec;
  --hex-gray:#6b6b6b;
  --dark:#1c1c1c;
  --white:#fff;
}
*{box-sizing:border-box;margin:0;padding:0}
html,body{width:1200px;height:2546px;overflow:hidden}
body{position:relative;font-family:"Lato",Arial,sans-serif;color:var(--ink);background:var(--white)}
.abs{position:absolute}

/* header */
.hero{position:absolute;left:0;top:0;width:1200px;height:662px;
  background:linear-gradient(180deg,#23331f 0%,#3f5a33 12%,#5f8348 22%,#2e5a7a 30%,#3e7a9e 36%,#6f9650 44%,#86a64c 55%,#b9b53c 68%,#d6c12b 78%,#7b8e2e 90%,#4f6a26 100%)}
.topbar{position:absolute;left:0;top:0;width:1200px;height:80px;background:rgba(20,28,20,.55)}
.brand-box{position:absolute;left:0;top:0;width:458px;height:158px;background:var(--white);
  clip-path:polygon(0 0,458px 0,394px 158px,0 158px);
  display:flex;align-items:center;padding-left:88px}
.brand-name{font-family:"Lato",sans-serif;font-weight:700;font-size:46px;color:var(--navy);letter-spacing:-.5px}
.contact-item{position:absolute;top:20px;display:flex;align-items:center;gap:12px;color:var(--white)}
.contact-item .label{font-size:12px;font-weight:700;line-height:1.5}
.contact-item .value{font-size:13px}
.nav{position:absolute;left:399px;top:80px;width:801px;height:78px;background:var(--green);
  clip-path:polygon(38px 0,801px 0,801px 78px,0 78px)}
.nav a{position:absolute;top:0;height:78px;line-height:78px;font-size:12.5px;color:var(--white);text-decoration:none;letter-spacing:.4px;transform:translateX(-50%)}
.nav a.active{background:var(--blue);width:66px;text-align:center;font-weight:700}
.hero-title{position:absolute;top:408px;left:0;width:1200px;text-align:center;color:var(--white);
  font-family:"Jost",sans-serif;font-weight:500;font-size:38px;letter-spacing:.5px;text-shadow:0 2px 4px rgba(0,0,0,.45)}

/* features */
.features{position:absolute;left:0;top:662px;width:1200px;height:243px;background:var(--gray-bg)}
.feature{position:absolute;top:-86px;width:300px;text-align:center;transform:translateX(-50%)}
.feature svg{display:block;margin:0 auto}
.feature h3{margin-top:30px;font-weight:400;font-size:16px;color:var(--ink);letter-spacing:.3px}
.feature p{margin-top:14px;font-size:12.5px;line-height:1.55;color:var(--text)}
.more{color:var(--green-dark)}

/* shared */
.section-title{position:absolute;left:0;width:1200px;text-align:center;font-size:29px;font-weight:400;color:var(--ink)}
.section-title span{color:var(--blue)}
.divider{position:absolute;left:430px;width:340px;height:14px}
.divider::before{content:"";position:absolute;left:0;right:0;top:6px;height:1px;background:#999}
.divider::after{content:"";position:absolute;left:163px;top:0;width:14px;height:14px;border-radius:50%;background:var(--white);border:1px solid #999}
.btn{position:absolute;height:34px;background:var(--green);color:var(--white);font-size:12.5px;font-weight:700;display:flex;align-items:center;gap:8px;padding:0 12px 0 4px}
.btn i{display:block;width:26px;height:26px;border-radius:50%;background:var(--white);border:3px solid var(--green-dark)}

/* about */
.about-mark{position:absolute;left:161px;top:942px;width:229px;height:259px;display:flex;align-items:center;justify-content:center}
.about-mark span{font-weight:700;font-size:48px;color:var(--navy)}
.about-rule{position:absolute;left:427px;top:942px;width:3px;height:240px;background:var(--green)}
.about-rule::after{content:"";position:absolute;left:3px;top:110px;border:8px solid transparent;border-left-color:var(--green)}
.about-title{position:absolute;left:462px;top:958px;font-size:29px;font-weight:400}
.about-title span{color:var(--blue)}
.about-sub{position:absolute;left:462px;top:1000px;width:100px;height:12px}
.about-sub::before{content:"";position:absolute;left:0;top:5px;width:100px;height:1px;background:#aaa}
.about-sub::after{content:"";position:absolute;left:0;top:0;width:12px;height:12px;border-radius:50%;background:var(--white);border:1px solid #999}
.body-copy{font-size:13px;line-height:1.65;color:var(--text);text-align:justify}

/* products */
.products{position:absolute;left:0;top:1236px;width:1200px;height:427px;background:var(--gray-bg)}
.product-frame{position:absolute;left:176px;top:1368px;width:334px;height:232px;border:1px solid #b5c48e}
.product-photo{position:absolute;left:161px;top:1375px;width:345px;height:230px;
  background:linear-gradient(135deg,#c9dbe8 0%,#9fbccf 35%,#eef3f6 60%,#7f9aae 100%)}
.product-name{position:absolute;left:540px;top:1374px;font-size:16px;font-weight:400;letter-spacing:.3px}
.arrow{position:absolute;top:1478px;width:0;height:0;border:11px solid transparent}
.arrow.prev{left:108px;border-right:12px solid #777;border-left:0}
.arrow.next{left:1070px;border-left:12px solid #777;border-right:0}

/* blogs */
.blog-photo{position:absolute;top:1807px;width:419px;height:185px;border:4px solid var(--navy)}
.blog-photo.factory{left:161px;background:linear-gradient(180deg,#55606a 0%,#a7b3bd 45%,#dfe3e6 70%,#8a7f86 100%)}
.blog-photo.pond{left:619px;background:linear-gradient(180deg,#9cc3e0 0%,#c9dbe6 35%,#5a8b3d 55%,#8fa86a 72%,#5b7d56 100%)}
.date{position:absolute;top:2016px;width:43px;text-align:center}
.date .day{height:28px;line-height:28px;background:#ddd;font-size:15px;color:var(--ink)}
.date .mon{height:30px;line-height:30px;background:var(--navy);font-size:12px;color:var(--white)}
.post-title{position:absolute;top:2016px;font-size:14px;letter-spacing:.2px}
.post-meta{position:absolute;top:2046px;display:flex;gap:14px;font-size:10px;color:#666}
.post-meta b{display:inline-block;width:8px;height:8px;border-radius:50%;background:var(--green);margin-right:4px;font-weight:400}
.post-text{position:absolute;top:2074px;width:400px;font-size:12.5px;line-height:1.6;color:var(--ink)}

/* footer */
.footer-blue{position:absolute;left:0;top:2211px;width:1200px;height:304px;background:var(--blue)}
.footer-dark{position:absolute;left:0;top:2211px;width:441px;height:335px;background:var(--dark);
  clip-path:polygon(0 0,441px 0,412px 335px,0 335px)}
.foot-head{position:absolute;top:2240px;font-family:"Jost",sans-serif;font-size:19px;color:var(--white);padding-bottom:10px;border-bottom:1px solid rgba(255,255,255,.7)}
.field{position:absolute;left:161px;width:231px;height:29px;background:var(--white);font-size:11px;color:#666;padding:7px 8px}
.submit{position:absolute;left:161px;top:2482px;height:32px;background:var(--green);color:var(--white);font-size:12.5px;font-weight:700;display:flex;align-items:center;gap:6px;padding:0 10px 0 3px}
.submit i{display:block;width:24px;height:24px;border-radius:50%;background:var(--dark);border:3px solid var(--green-dark)}
.links{position:absolute;left:502px;top:2296px;list-style:none}
.links li{height:31px;font-size:12px;color:var(--white);padding-left:14px;position:relative}
.links li::before{content:"";position:absolute;left:0;top:4px;border:4px solid transparent;border-left:5px solid var(--white)}
.contact-row{position:absolute;left:641px;display:flex;gap:14px;color:var(--white);font-size:12px;line-height:1.5}
.foot-brand{position:absolute;left:848px;top:2310px;width:191px;text-align:center;font-weight:700;font-size:44px;color:var(--white)}
.copyright{position:absolute;left:412px;top:2515px;width:788px;height:31px;background:var(--dark);color:#ddd;font-size:12px;line-height:31px;text-align:center;padding-right:170px}
</style>
</head>
<body>

<header>
  <div class="hero" role="img" aria-label="Mountain lake surrounded by pine forest with yellow wildflowers in the foreground"></div>
  <div class="topbar"></div>
  <div class="brand-box"><span class="brand-name">Pimbrook</span></div>

  <div class="contact-item" style="left:622px">
    <svg width="44" height="44" viewBox="0 0 44 44"><circle cx="22" cy="22" r="20" fill="none" stroke="#8dbf3e" stroke-width="2.5"/><path d="M15 12c2 0 3 4 3 5s-2 2-2 3c1 3 4 6 7 7 1 0 2-2 3-2s5 1 5 3-2 4-4 4c-7 0-15-8-15-15 0-2 2-5 3-5z" fill="#8dbf3e"/></svg>
    <div><div class="label">We're on call 24/7</div><div class="value">(123) 123 456 7890</div></div>
  </div>
  <div class="contact-item" style="left:833px">
    <svg width="46" height="34" viewBox="0 0 46 34"><rect x="2" y="2" width="42" height="30" fill="none" stroke="#8dbf3e" stroke-width="2.5"/><path d="M2 2l21 17L44 2M2 32l15-14M44 32L29 18" fill="none" stroke="#8dbf3e" stroke-width="2.5"/></svg>
    <div><div class="label">Send us a mail</div><div class="value">office@pimbrookinc.com</div></div>
  </div>

  <nav class="nav">
    <a class="active" style="left:89px">HOME</a>
    <a style="left:185px">ABOUT US</a>
    <a style="left:290px">SERVICES</a>
    <a style="left:398px">PRODUCTS</a>
    <a style="left:495px">BLOG</a>
    <a style="left:598px">CONTACT US</a>
  </nav>

  <h1 class="hero-title">BEST PIMBROOK INC PRODUCTS</h1>
</header>

<section class="features">
  <div class="feature" style="left:285px">
    <svg width="150" height="165" viewBox="0 0 150 165"><polygon points="75,4 145,43 145,122 75,161 5,122 5,43" fill="#6b6b6b"/><polygon points="75,20 130,51 130,114 75,145 20,114 20,51" fill="#fff"/></svg>
    <h3>RESEARCH / SOURCE</h3>
    <p>Lorem ipsum dolor sit amet,<br>consectetuer adipiscing elit...<span class="more">[+]</span></p>
  </div>
  <div class="feature" style="left:599px">
    <svg width="150" height="165" viewBox="0 0 150 165"><polygon points="75,4 145,43 145,122 75,161 5,122 5,43" fill="#1d5a99"/><polygon points="75,20 130,51 130,114 75,145 20,114 20,51" fill="#fff"/></svg>
    <h3>PURE / SUSTAINABLE</h3>
    <p>Lorem ipsum dolor sit amet,<br>consectetuer adipiscing elit...<span class="more">[+]</span></p>
  </div>
  <div class="feature" style="left:913px">
    <svg width="150" height="165" viewBox="0 0 150 165"><polygon points="75,4 145,43 145,122 75,161 5,122 5,43" fill="#6b6b6b"/><polygon points="75,20 130,51 130,114 75,145 20,114 20,51" fill="#fff"/></svg>
    <h3>SUPPLY</h3>
    <p>Lorem ipsum dolor sit amet,<br>consectetuer adipiscing elit...<span class="more">[+]</span></p>
  </div>
</section>

<section class="about">
  <div class="about-mark"><span>Pimbrook</span></div>
  <div class="about-rule"></div>
  <h2 class="about-title">ABOUT <span>PIMBROOK INC.</span></h2>
  <div class="about-sub"></div>
  <p class="body-copy abs" style="left:462px;top:1034px;width:576px">Lorem ipsum dolor sit amet, consectetuer adipiscing elit, sed diam nonummy nibh euismod tincidunt ut laoreet dolore magna aliquam erat volutpat. Ut wisi enim ad minim veniam, quis nostrud exerci tation ullamcorper suscipit lobortis nisl ut aliquip ex ea commodo consequat. Duis autem vel eum iriure dolor in hendrerit in vulputate velit esse molestie consequat.</p>
  <div class="btn" style="left:462px;top:1142px"><i></i>Read More »</div>
</section>

<section class="products"></section>
<h2 class="section-title" style="top:1288px">OUR <span>PRODUCTS</span></h2>
<div class="divider" style="top:1331px"></div>
<div class="arrow prev"></div>
<div class="product-frame"></div>
<div class="product-photo" role="img" aria-label="Laboratory spatula holding white powder over a perforated tray"></div>
<h3 class="product-name">HYALURONIC ACID</h3>
<p class="body-copy abs" style="left:544px;top:1412px;width:496px">Lorem ipsum dolor sit amet, consectetuer adipiscing elit, sed diam nonummy nibh euismod tincidunt ut laoreet dolore magna aliquam erat volutpat. Ut wisi enim ad minim veniam, quis nostrud exerci tation ullamcorper suscipit lobortis nisl ut aliquip ex ea commodo consequat. Duis autem vel eum iriure dolor in hendrerit in vulputate velit esse molestie consequat, vel illum dolore eu feugiat nulla facilisis at vero eros et accumsan et iusto odio dignissim qui blandit praesent luptatum zzril delenit augue.</p>
<div class="btn" style="left:540px;top:1573px"><i></i>Read More »</div>
<div class="arrow next"></div>

<section class="blogs">
  <h2 class="section-title" style="top:1716px">LATEST <span>BLOGS</span></h2>
  <div class="divider" style="top:1759px"></div>

  <div class="blog-photo factory" role="img" aria-label="Bottling machinery in a clean production hall"></div>
  <div class="date" style="left:161px"><div class="day">16</div><div class="mon">Apr</div></div>
  <h3 class="post-title" style="left:229px">LOREM IPSUM DOLOR SIT AMET.</h3>
  <div class="post-meta" style="left:229px"><span><b></b>Mara Quill</span><span><b></b>Blog</span><span><b></b>1 Comments</span></div>
  <p class="post-text" style="left:229px">Lorem ipsum dolor sit amet, consectetuer adipiscing elit, sed diam nonummy nibh volutpat veniam.</p>
  <div class="btn" style="left:226px;top:2125px"><i></i>Read More »</div>

  <div class="blog-photo pond" role="img" aria-label="Garden pond with mountains and trees under a blue sky"></div>
  <div class="date" style="left:619px"><div class="day">16</div><div class="mon">Apr</div></div>
  <h3 class="post-title" style="left:686px">LOREM IPSUM DOLOR SIT AMET.</h3>
  <div class="post-meta" style="left:686px"><span><b></b>Mara Quill</span><span><b></b>Blog</span><span><b></b>1 Comments</span></div>
  <p class="post-text" style="left:686px">Lorem ipsum dolor sit amet, consectetuer adipiscing elit, sed diam nonummy nibh volutpat veniam.</p>
  <div class="btn" style="left:684px;top:2125px"><i></i>Read More »</div>
</section>

<footer>
  <div class="footer-blue"></div>
  <div class="footer-dark"></div>

  <h4 class="foot-head" style="left:161px;width:238px">Quick Contact</h4>
  <div class="field" style="top:2293px">Name</div>
  <div class="field" style="top:2330px">Email</div>
  <div class="field" style="top:2367px">Phone</div>
  <div class="field" style="top:2405px;height:61px">Comment</div>
  <div class="submit"><i></i>SUBMIT</div>

  <h4 class="foot-head" style="left:502px;width:116px">Quick Links</h4>
  <ul class="links">
    <li>Home</li><li>About Us</li><li>Services</li><li>Products</li><li>Blog</li><li>Contact Us</li>
  </ul>

  <h4 class="foot-head" style="left:641px;width:176px">Contact Us</h4>
  <div class="contact-row" style="top:2298px">
    <svg width="26" height="26" viewBox="0 0 26 26"><rect width="26" height="26" rx="3" fill="#fff"/><path d="M13 5a6 6 0 0 0-6 6c0 5 6 10 6 10s6-5 6-10a6 6 0 0 0-6-6z" fill="#34a7d8"/><circle cx="13" cy="11" r="2.2" fill="#fff"/></svg>
    <div style="width:140px">Duis autem vel eum iriure dolor in hendrerit in velit essem molestie</div>
  </div>
  <div class="contact-row" style="top:2385px;align-items:center">
    <svg width="26" height="26" viewBox="0 0 26 26"><rect width="26" height="26" rx="3" fill="#fff"/><path d="M8 6c1.5 0 2.5 3 2.5 4s-1.5 1.5-1.5 2.5c1 2.5 3 4.5 5.5 5.5 1 0 1.5-1.5 2.5-1.5s4 1 4 2.5-1.5 3-3 3C12 22 4 14 4 9c0-1.5 2.5-3 4-3z" fill="#34a7d8"/></svg>
    <div>(123) 123 456 7890</div>
  </div>
  <div class="contact-row" style="top:2448px;align-items:center">
    <svg width="26" height="26" viewBox="0 0 26 26"><rect width="26" height="26" rx="3" fill="#fff"/><rect x="5" y="8" width="16" height="11" fill="none" stroke="#34a7d8" stroke-width="1.8"/><path d="M5 8l8 6 8-6" fill="none" stroke="#34a7d8" stroke-width="1.8"/></svg>
    <div>office@pimbrookinc.com</div>
  </div>

  <div class="foot-brand">Pimbrook</div>

  <div class="copyright">Copyright © 2016 Pimbrookinc.  All Right Reserved</div>
</footer>

</body>
</html>
```